Business Card Design Project

1. Show the company logo.
2. Only company email ID and website address to be shown (office@tikhayavolna.fm , www.tikhayavolna.fm).
3. Logo to be provided by us, 2 designs just in case. The logo is made with ' Tikhaya Volna' text, need to be edited so that it shows 'Yasnaya Afisha' instead .
4. Single sided business card, portrait or landscape is not a problem; back side to be filled with colors or a design that matches the logo the best.
5. Logo is to be embossed.
6. We're looking at an English and Russian version.
7. any other better idea is always welcomed.

```html
<!DOCTYPE html>
<html lang="en">
<head>
<meta charset="utf-8">
<title>Business Card – Front and Back</title>
<link rel="stylesheet" href="https://fonts.googleapis.com/css2?family=Montserrat:wght@700&family=Arimo:wght@700&display=swap">
<style>
  :root {
    --stage-top: #3e4949;
    --stage-bottom: #b7bbb9;
    --card-dark: #3b4647;
    --card-light: #ffffff;
    --accent-blue: #0a5cff;
    --text-light: #ffffff;
    --wave-dark: rgba(150, 170, 185, 0.16);
    --wave-light: rgba(120, 150, 230, 0.10);
  }
  * { margin: 0; padding: 0; box-sizing: border-box; }
  html, body {
    width: 1200px;
    height: 800px;
    overflow: hidden;
  }
  body {
    position: relative;
    background: linear-gradient(180deg, var(--stage-top) 0%, var(--stage-bottom) 100%);
  }
  .card {
    position: absolute;
    top: 60px;
    width: 490px;
    height: 686px;
    border-radius: 20px;
    overflow: hidden;
  }
  .card--front { left: 50px; background: var(--card-dark); }
  .card--back { left: 660px; background: var(--card-light); }

  .wave-decor {
    position: absolute;
    left: 0;
    top: 190px;
    width: 490px;
    height: 420px;
  }
  .card--front .wave-decor {
    background: radial-gradient(ellipse 70% 45% at 40% 40%, var(--wave-dark), transparent 70%);
  }
  .card--back .wave-decor {
    background: radial-gradient(ellipse 75% 50% at 40% 45%, var(--wave-light), transparent 70%);
  }

  .brand-name {
    position: absolute;
    left: 0;
    right: 0;
    top: 290px;
    text-align: center;
    white-space: nowrap;
    font-family: "Montserrat", sans-serif;
    font-weight: 700;
    font-size: 44px;
    line-height: 56px;
    letter-spacing: -0.5px;
    color: var(--text-light);
  }

  .contact {
    position: absolute;
    left: 0;
    right: 0;
    top: 556px;
    text-align: center;
    font-family: "Arimo", sans-serif;
    font-weight: 700;
    font-size: 20px;
    line-height: 24px;
    color: var(--text-light);
    list-style: none;
  }

  .accent-band {
    position: absolute;
    left: 190px;
    top: 0;
    width: 116px;
    height: 100%;
    background: var(--accent-blue);
  }
</style>
</head>
<body>
  <section class="card card--front" aria-label="Card front">
    <div class="wave-decor" role="img" aria-label="Faint flowing line wave pattern"></div>
    <h1 class="brand-name">Yasnaya Afisha</h1>
    <ul class="contact">
      <li>office@tikhayavolna.fm</li>
      <li>www.tikhayavolna.fm</li>
    </ul>
  </section>

  <section class="card card--back" aria-label="Card back">
    <div class="wave-decor" role="img" aria-label="Faint flowing line wave pattern"></div>
    <div class="accent-band"></div>
  </section>
</body>
</html>
```